Managed IT services business card design

We haven't needed a business card since the founding of the business in 2005. All our clients have been coming through word of mouth. And lately more and more existing clients are requesting for our business cards to pass on to their contacts in recommending us.
So we needing a business card design. We use various innovative solutions and methodologies to provide IT services to small businesses in managing their IT systems. Our role is the same as an in-house, full-time IT Manager for our clients, but outsourced. So we take care of all our clients' IT needs, just as an IT Manager would be expected to perform.
We have a holding website, which we're happy to leave for now. If we can use the same logo would be great - www.lomvex.com.au
Preferred colours are shades of are white, grey and black.
We pride our business with the following traits: proactive, good service, prompt response, trustworthy.
Target Market(s)
Small businesses of any industry
Industry/Entity Type
Business

```html
<!DOCTYPE html>
<html lang="en">
<head>
<meta charset="utf-8">
<title>lomvex business card</title>
<link rel="stylesheet" href="https://fonts.googleapis.com/css2?family=Inter:wght@300;400&display=swap">
<style>
  :root {
    --stage: #2e2e30;
    --paper: #ffffff;
    --ink: #141414;
    --black: #0d0d0d;
    --grey-light: #6e6e6e;
    --grey-dark: #474747;
    --muted: #8c8c8c;
    --sub: #5a5a5a;
    --light-text: #f2f2f2;
  }
  * { margin: 0; padding: 0; box-sizing: border-box; }
  html, body {
    width: 1200px; height: 900px; overflow: hidden;
    background: var(--stage);
    font-family: "Inter", "Helvetica Neue", Arial, sans-serif;
  }
  .card {
    position: absolute; left: 153px; top: 201px;
    width: 894px; height: 498px;
    background: var(--grey-dark);
    overflow: hidden;
  }
  .card-shapes { position: absolute; inset: 0; width: 100%; height: 100%; }
  .brand {
    position: absolute; left: 424px; top: 34px;
    display: flex; align-items: center; gap: 30px;
  }
  .brand-name {
    font-weight: 300; font-size: 68px; line-height: 1;
    letter-spacing: 0.2em; color: var(--ink);
  }
  .brand-mark { width: 20px; height: 20px; background: var(--ink); margin-top: 10px; }
  .brand-line {
    position: absolute; left: 424px; top: 120px;
    font-size: 15px; font-weight: 300; color: var(--sub);
  }
  .contact-list {
    position: absolute; left: 66px; top: 340px;
    list-style: none; color: var(--light-text);
    font-size: 15px; font-weight: 300;
  }
  .contact-list li { display: flex; align-items: center; gap: 18px; height: 35px; }
  .contact-icon { width: 22px; height: 22px; }
  .tagline {
    position: absolute; left: 586px; top: 400px;
    font-size: 15px; font-weight: 300; line-height: 24px; color: var(--muted);
  }
</style>
</head>
<body>
  <section class="card">
    <svg class="card-shapes" viewBox="0 0 447 249" preserveAspectRatio="none">
      <defs>
        <linearGradient id="facet-tone" x1="0" y1="0" x2="1" y2="1">
          <stop offset="0" stop-color="#6e6e6e"/>
          <stop offset="0.55" stop-color="#5c5c5c"/>
          <stop offset="1" stop-color="#474747"/>
        </linearGradient>
      </defs>
      <rect class="facet-field" width="447" height="249" fill="url(#facet-tone)" role="img" aria-label="Grey low-poly faceted pattern"/>
      <polygon class="paper-panel" points="92,0 447,0 447,86 307,172" fill="var(--paper)"/>
      <polygon class="black-panel" points="447,86 447,249 182,249" fill="var(--black)"/>
    </svg>

    <div class="brand">
      <span class="brand-name">lomvex</span>
      <span class="brand-mark"></span>
    </div>
    <p class="brand-line">managed i.t. services and consulting</p>

    <ul class="contact-list">
      <li>
        <svg class="contact-icon" viewBox="0 0 24 24" fill="none" stroke="currentColor" stroke-width="1.6" stroke-linecap="round" stroke-linejoin="round">
          <path d="M17 3l3 3-3 4-2-1c-1 2-4 5-6 6l1 2-4 3-3-3c1-7 7-13 14-14z"/>
        </svg>
        <span>+61 4000 182 475</span>
      </li>
      <li>
        <svg class="contact-icon" viewBox="0 0 24 24" fill="none" stroke="currentColor" stroke-width="1.6" stroke-linejoin="round">
          <rect x="3" y="5" width="18" height="14"/>
          <path d="M3 5l9 8 9-8M3 19l7-7M21 19l-7-7"/>
        </svg>
        <span>mail@lomvex.com.au</span>
      </li>
      <li>
        <svg class="contact-icon" viewBox="0 0 24 24" fill="none" stroke="currentColor" stroke-width="1.6">
          <path d="M12 22s-7-7-7-12a7 7 0 0 1 14 0c0 5-7 12-7 12z"/>
          <circle cx="12" cy="10" r="2.5"/>
        </svg>
        <span>little harlow, kelbourne</span>
      </li>
    </ul>

    <p class="tagline">proactive, good service,<br>prompt response &amp; trustworthy</p>
  </section>
</body>
</html>
```